Hand-Crafted Furniture Company

We are working with Brokkhalm to build a new website for them.

Some sites to use for content/competitors and inspiration:

https://vastrupfurniture.com
https://tulverhome.com
https://www.kenbrickle.com
https://www.dunmarrowoodworks.com

Thank you for taking the time to consider designing a website for us. We are web developers based in Stockton, CA, USA. Most of our projects go through the same process. Understanding this process may help you win a project with us. We custom-code all of our websites in-house. We don’t have any requirements as to what tools you use for your design, but we prefer Figma files. For any design that we label as four stars, we send it to the client for review. The client picks the final design they want us to use. Once we complete this process, we will continue to show additional clients all the four-star sites and purchase them later. Your designs will have multiple chances to sell. For better chances of success, we ask that you follow these guidelines.

IMAGES:
If you use any images or icons in the design, we ask that you have a link to the asset so we can purchase the image/icon. Most of the designs we submit do not have the customer’s images on them unless they have some great images. Be creative; show us the feeling you are trying to portray with your image choices. Use any royalty-free site you choose. We subscribe to Quiver and mainly use their images, but we can purchase images outside of Quiver. PLEASE NOTE: we will not submit designs to clients with watermarks on the images.

FONTS:
We ask that you identify the fonts used in the design. This can be done in a message if you want. We typically use Pellat Fonts and Quiver Fonts.

CONTENT:
We're always open to different content and ideas. We often submit designs with stock images so the client can see our vision. We typically take pictures after the website launch to use their images with our vision. Lorem Ipsum is fine for paragraphs, but we ask that you write the headers in correct English. We want to be able to show the vision and identify the sections of the website.

INSPIRATION:
We typically add a couple of links in the brief of websites we like to help you get started in your design.

REVISIONS:
We do not often ask for revisions of the designs unless we see something in the design that may not appeal to the client. If there are slight changes that we want to make, we do that in the development process.

FEEDBACK:
We rarely give feedback on designs during the design process. We are working on many website projects and do not have the time to provide feedback. We usually respond if your request is well thought out and asks specific questions, but a note asking “feedback, please” usually goes unanswered.

```html
<!DOCTYPE html>
<html lang="en">
<head>
<meta charset="utf-8">
<title>Brokkhalm – Hand-Crafted Furniture</title>
<link rel="stylesheet" href="https://fonts.googleapis.com/css2?family=Montserrat:wght@400;500;600&family=Ubuntu:wght@400;500&family=Righteous&display=swap">
<style>
:root{
  --brown:#6a4430;
  --brown-dark:#5e3c29;
  --brown-box:#654431;
  --brown-light:#7a5440;
  --ink:#2b2b2b;
  --muted:#444;
  --line:#6a4430;
  --white:#fff;
  --black:#111;
}
*{margin:0;padding:0;box-sizing:border-box}
html,body{width:1200px;height:3579px;overflow:hidden}
body{position:relative;background:var(--white);font-family:"Montserrat",sans-serif;color:var(--ink)}
.abs{position:absolute}
a{color:inherit;text-decoration:none}

/* header */
.top-call{left:111px;top:37px;font-size:13px;display:flex;align-items:center;gap:14px;letter-spacing:.2px}
.brand{left:0;width:1200px;top:14px;text-align:center;font-family:"Montserrat",sans-serif;font-weight:600;font-size:44px;color:var(--brown);letter-spacing:1px}
.brand .dot{display:inline-block;width:7px;height:7px;background:#b98a6c;margin-left:4px}
.search{left:936px;top:37px;font-size:13px;display:flex;gap:32px;align-items:center}
.nav{left:111px;width:978px;top:99px;display:flex;justify-content:space-between;font-size:15px;letter-spacing:.2px}
.nav .active{color:var(--brown);position:relative}
.nav .active::after{content:"";position:absolute;left:0;right:0;top:26px;height:4px;background:var(--brown)}
.header-rule{left:0;top:136px;width:1200px;height:1px;background:#ddd}

/* hero */
.hero{left:0;top:136px;width:1200px;height:507px;background:linear-gradient(160deg,#4a4642,#2c2a28 45%,#3a3430 70%,#27231f)}
.hero-eyebrow{left:0;width:1200px;top:274px;text-align:center;color:var(--white);font-size:22px;font-weight:500;letter-spacing:.5px}
.hero-title{left:267px;top:336px;width:668px;height:57px;background:var(--brown);display:flex;align-items:center;justify-content:center;font-family:"Righteous",sans-serif;font-size:46px;letter-spacing:2px;color:transparent;-webkit-text-stroke:1.6px #fff}
.hero-copy{left:130px;width:940px;top:427px;text-align:center;color:var(--white);font-size:15px;line-height:39px}

/* feature cards */
.card{top:657px;height:257px}
.card span{position:absolute;left:43px;top:44px;color:var(--white);font-weight:600;font-size:17px;letter-spacing:.5px}
.card-1{left:0;width:390px;background:linear-gradient(120deg,#e9e9e9,#d7d5d1 60%,#bfb7a8)}
.card-2{left:400px;width:399px;background:linear-gradient(120deg,#d9ccb9,#cdbba2 50%,#8d6444)}
.card-3{left:810px;width:390px;background:linear-gradient(120deg,#6a6663,#4f4b48 60%,#3a3432)}

/* about */
.about-frame{left:111px;top:1000px;width:411px;height:267px;border:1px solid #555;border-radius:2px}
.about-frame::before{content:"";position:absolute;left:4px;top:4px;width:225px;height:8px;background:var(--brown)}
.about-img{left:122px;top:1011px;width:489px;height:371px;background:linear-gradient(150deg,#a5b05c,#6f6a2e 40%,#8b4a25 70%,#5a3520)}
.section-title{font-family:"Ubuntu",sans-serif;font-weight:500;color:var(--brown);letter-spacing:-.3px}
.about-title{left:674px;top:992px;font-size:31px;display:flex;align-items:center;gap:18px}
.about-title i{display:block;width:73px;height:2px;background:var(--line)}
.about-copy{left:674px;top:1045px;width:440px;font-size:15px;line-height:38.5px;color:var(--muted)}
.btn{background:var(--brown);color:var(--white);font-size:16px;font-weight:600;display:flex;align-items:center;justify-content:center;border-radius:3px;box-shadow:0 2px 0 #3b2418;letter-spacing:.3px}
.about-btn{left:674px;top:1339px;width:152px;height:43px}

/* video */
.video{left:0;top:1469px;width:1200px;height:417px;background:linear-gradient(180deg,#dcdcd6,#bfbdb6 45%,#c48a52 75%,#b77b44)}
.play{left:561px;top:1639px}

/* occasion */
.occasion-title{left:0;width:1200px;top:1966px;font-size:33px;display:flex;justify-content:center;align-items:center;gap:22px}
.occasion-title i{display:block;width:74px;height:2px;background:var(--line)}
.occasion-title .spacer{width:74px}
.chair-title{left:113px;top:2069px;font-size:28px}
.chair-copy{left:113px;top:2124px;width:420px;font-size:15px;line-height:38.5px;color:var(--muted)}
.swatch{top:2420px;width:44px;height:44px;border-radius:50%}
.sw-1{left:113px;background:var(--brown);box-shadow:0 0 0 3px #fff,0 0 0 5px var(--brown)}
.sw-2{left:173px;background:#000}
.sw-3{left:234px;background:#3a6236}
.sw-4{left:293px;background:#7c1a42}
.chair-btn{left:113px;top:2507px;width:152px;height:43px}
.chair-img{left:600px;top:2060px;width:488px;height:389px;border-radius:4px;background:linear-gradient(135deg,#c8b9a2,#b6a488 50%,#8a6648)}
.thumb{top:2468px;width:100px;height:91px}
.th-1{left:622px;background:linear-gradient(135deg,#c4b49a,#8b6a4b);box-shadow:0 0 0 2px var(--brown)}
.th-2{left:736px;background:linear-gradient(135deg,#eeeeee,#dcd7d0)}
.th-3{left:851px;background:linear-gradient(135deg,#5c1d3b,#3a1a20)}
.th-4{left:965px;background:linear-gradient(135deg,#eef0ee,#c9cdc6)}
.carousel-prev{left:592px;top:2503px}
.carousel-next{left:1081px;top:2503px}

/* testimonials */
.testi-title{left:0;width:1200px;top:2629px;font-size:33px;display:flex;justify-content:center;align-items:center;gap:22px}
.testi-title i{display:block;width:74px;height:2px;background:var(--line)}
.testi-title .spacer{width:74px}
.testi-box{left:111px;top:2722px;width:977px;height:474px;background:var(--brown-box);overflow:hidden}
.testi-box svg{position:absolute;left:0;top:0}
.portrait-ring{left:180px;top:2777px;width:362px;height:362px;border-radius:50%;border:2px solid #f1e8e0}
.portrait{left:187px;top:2784px;width:348px;height:348px;border-radius:50%;background:radial-gradient(circle at 50% 70%,#6fa2c7,#e8e8e8 62%)}
.quote-mark{left:604px;top:2775px;color:var(--white);font-family:"Ubuntu",sans-serif;font-size:96px;line-height:1}
.testi-copy{left:606px;top:2849px;width:440px;color:var(--white);font-size:15px;line-height:38.5px}
.testi-arrows{left:606px;top:3086px;display:flex;gap:36px}
.testi-name{left:760px;width:156px;top:3066px;text-align:right;color:var(--white);font-size:16px;line-height:35px}
.avatar{left:943px;top:3061px;width:72px;height:72px;border-radius:50%;background:radial-gradient(circle at 50% 75%,#6fa2c7,#ececec 60%);border:2px solid #fff}

/* footer */
.foot-brand{left:111px;top:3281px;font-weight:600;font-size:52px;color:var(--brown);letter-spacing:1px}
.foot-brand .dot{display:inline-block;width:8px;height:8px;background:#b98a6c;margin-left:4px}
.social{top:3389px;width:34px;height:34px;border-radius:50%;border:1.5px solid #333}
.so-1{left:111px}.so-2{left:150px}.so-3{left:190px}
.foot-head{top:3280px;font-size:17px;font-weight:500;color:var(--brown);letter-spacing:.3px}
.foot-list{top:3333px;font-size:13px;line-height:37px;letter-spacing:.3px}
.contact-list{left:928px;top:3333px;font-size:13px;line-height:37px;letter-spacing:.3px}
.contact-list li{list-style:none;display:flex;align-items:center}
.contact-list .ic{width:30px;display:inline-flex}
ul{list-style:none}
.bottom-bar{left:0;top:3514px;width:1200px;height:65px;background:var(--black);color:var(--white);font-size:13px;font-weight:500;display:flex;align-items:center;justify-content:center;letter-spacing:.3px}
</style>
</head>
<body>

<header>
  <div class="abs top-call">
    <svg width="14" height="14" viewBox="0 0 24 24"><path fill="#111" d="M6.6 10.8a15.1 15.1 0 0 0 6.6 6.6l2.2-2.2c.3-.3.7-.4 1-.2 1.1.4 2.3.6 3.6.6.6 0 1 .4 1 1V20c0 .6-.4 1-1 1A17 17 0 0 1 3 4c0-.6.4-1 1-1h3.5c.6 0 1 .4 1 1 0 1.3.2 2.5.6 3.6.1.3 0 .7-.2 1z"/></svg>
    <span>CALL US ; +1 888 888 8888</span>
  </div>
  <div class="abs brand">brokkhalm<span class="dot"></span></div>
  <div class="abs search">
    <span>SEARCH HERE...</span>
    <svg width="14" height="14" viewBox="0 0 24 24" fill="none" stroke="#111" stroke-width="2.4"><circle cx="10" cy="10" r="7"/><path d="M15 15l6 6"/></svg>
  </div>
  <nav class="abs nav">
    <a class="active" href="#">HOME</a><a href="#">ABOUT</a><a href="#">DINING</a><a href="#">LIVING</a><a href="#">BEDROOM</a><a href="#">OFFICE</a><a href="#">FEATURED</a><a href="#">CONTRACT</a>
  </nav>
  <div class="abs header-rule"></div>
</header>

<section>
  <div class="abs hero" role="img" aria-label="Dimmed photo of a modern kitchen with a wooden dining table and dark chairs"></div>
  <p class="abs hero-eyebrow">WELCOME TO BROKKHALM</p>
  <h1 class="abs hero-title">HAND-CRAFTED FURNITURE</h1>
  <p class="abs hero-copy">Lorem ipsum dolor sit amet, consectetur adipiscing elit, sed do eiusmod tempor incididunt ut labore et dolore magna<br>aliqua. Ut enim ad minim veniam, quis nostrud exercitation ullamco laboris nisi ut aliquip<br>ex ea commodo consequat.</p>
</section>

<section>
  <div class="abs card card-1" role="img" aria-label="Light wooden chair with folded knit blankets"><span>LOREM IPSUM</span></div>
  <div class="abs card card-2" role="img" aria-label="Lounge chair beside a tree-stump side table"><span>LOREM IPSUM</span></div>
  <div class="abs card card-3" role="img" aria-label="Modern dark wooden armchair"><span>LOREM IPSUM</span></div>
</section>

<section>
  <div class="abs about-frame"></div>
  <div class="abs about-img" role="img" aria-label="Wooden rocking chair with a quilt on a sunny garden porch"></div>
  <h2 class="abs section-title about-title">ABOUT US <i></i></h2>
  <p class="abs about-copy">Lorem ipsum dolor sit amet, consectetur adipiscing elit, sed do eiusmod tempor incididunt ut labore et dolore magna aliqua. Ut enim ad minim veniam, quis nostrud exercitation ullamco laboris nisi ut aliquip<br>ex ea commodo consequat. Sed ut perspiciatis unde omnis iste natus error sit voluptatem accusantium doloremque laudantium.</p>
  <a class="abs btn about-btn" href="#">LEARN MORE</a>
</section>

<section>
  <div class="abs video" role="img" aria-label="Video still of a bright living room with a wooden table and TV cabinet"></div>
  <svg class="abs play" width="78" height="78" viewBox="0 0 78 78"><circle cx="39" cy="39" r="39" fill="#5a3a28" fill-opacity=".85"/><path d="M31 26l22 13-22 13z" fill="#fff"/></svg>
</section>

<section>
  <h2 class="abs section-title occasion-title"><i></i>SOMETHING FOR EVERY OCCASION<span class="spacer"></span></h2>
  <h3 class="abs section-title chair-title">THE CHAIR COLLECTIONS</h3>
  <p class="abs chair-copy">Lorem ipsum dolor sit amet, consectetur adipiscing elit, sed do eiusmod tempor incididunt ut labore et dolore magna aliqua. Ut enim ad minim veniam, quis nostrud exercitation ullamco laboris nisi ut aliquip<br>ex ea commodo consequat. Sed ut perspiciatis unde omnis iste natus error sit voluptatem accusantium doloremque laudantium.</p>
  <span class="abs swatch sw-1"></span><span class="abs swatch sw-2"></span><span class="abs swatch sw-3"></span><span class="abs swatch sw-4"></span>
  <a class="abs btn chair-btn" href="#">VIEW DETAILS</a>
  <div class="abs chair-img" role="img" aria-label="Wooden armchair with cream cushions against a plaster wall"></div>
  <svg class="abs carousel-prev" width="16" height="24" viewBox="0 0 16 24"><path d="M12 3L4 12l8 9" fill="none" stroke="#111" stroke-width="2.4"/></svg>
  <div class="abs thumb th-1" role="img" aria-label="Armchair thumbnail"></div>
  <div class="abs thumb th-2" role="img" aria-label="Round wooden side table thumbnail"></div>
  <div class="abs thumb th-3" role="img" aria-label="Dark desk against a purple wall thumbnail"></div>
  <div class="abs thumb th-4" role="img" aria-label="Dining table with linen cloth thumbnail"></div>
  <svg class="abs carousel-next" width="16" height="24" viewBox="0 0 16 24"><path d="M4 3l8 9-8 9" fill="none" stroke="#111" stroke-width="2.4"/></svg>
</section>

<section>
  <h2 class="abs section-title testi-title"><i></i>TESTIMONIALS<span class="spacer"></span></h2>
  <div class="abs testi-box">
    <svg width="977" height="474" viewBox="0 0 977 474"><path d="M0 474L440 0H0z" fill="#6e4a35"/></svg>
  </div>
  <div class="abs portrait-ring"></div>
  <div class="abs portrait" role="img" aria-label="Portrait of a smiling customer in a blue t-shirt"></div>
  <div class="abs quote-mark">“</div>
  <p class="abs testi-copy">Lorem ipsum dolor sit amet, consectetur adipiscing elit, sed do eiusmod tempor incididunt ut labore et dolore magna aliqua. Ut enim ad minim veniam, quis nostrud exercitation ullamco laboris nisi ut aliquip<br>ex ea commodo consequat.</p>
  <div class="abs testi-arrows">
    <svg width="36" height="20" viewBox="0 0 36 20"><path d="M35 10H2M10 2L2 10l8 8" fill="none" stroke="#fff" stroke-width="2"/></svg>
    <svg width="36" height="20" viewBox="0 0 36 20"><path d="M1 10h33M26 2l8 8-8 8" fill="none" stroke="#fff" stroke-width="2"/></svg>
  </div>
  <p class="abs testi-name">LOREM LIPSUM<br>MANAGAR</p>
  <div class="abs avatar" role="img" aria-label="Small customer avatar"></div>
</section>

<footer>
  <div class="abs foot-brand">brokkhalm<span class="dot"></span></div>
  <span class="abs social so-1" aria-label="Social link"></span>
  <span class="abs social so-2" aria-label="Social link"></span>
  <span class="abs social so-3" aria-label="Social link"></span>

  <h4 class="abs foot-head" style="left:431px">QUICK LINKS</h4>
  <ul class="abs foot-list" style="left:431px"><li>HOME</li><li>ABOUT</li><li>DINING</li><li>LIVING</li></ul>
  <ul class="abs foot-list" style="left:535px"><li>BEDROOM</li><li>OFFICE</li><li>FEATURED</li><li>CONTRACT</li></ul>

  <h4 class="abs foot-head" style="left:711px">OTHER LINKS</h4>
  <ul class="abs foot-list" style="left:711px"><li>FAQ</li><li>CAREERS</li><li>PRIVACY POLICY</li></ul>

  <h4 class="abs foot-head" style="left:928px">CONTACT US</h4>
  <ul class="abs contact-list">
    <li><span class="ic"><svg width="12" height="12" viewBox="0 0 24 24"><path fill="#111" d="M6.6 10.8a15.1 15.1 0 0 0 6.6 6.6l2.2-2.2c.3-.3.7-.4 1-.2 1.1.4 2.3.6 3.6.6.6 0 1 .4 1 1V20c0 .6-.4 1-1 1A17 17 0 0 1 3 4c0-.6.4-1 1-1h3.5c.6 0 1 .4 1 1 0 1.3.2 2.5.6 3.6.1.3 0 .7-.2 1z"/></svg></span>+1 888 888 8888</li>
    <li><span class="ic"><svg width="12" height="10" viewBox="0 0 24 18"><rect x="1" y="1" width="22" height="16" fill="none" stroke="#111" stroke-width="2.4"/><path d="M1 1l11 9 11-9" fill="none" stroke="#111" stroke-width="2.4"/></svg></span>INFO@LOREM.COM</li>
    <li><span class="ic"><svg width="11" height="14" viewBox="0 0 18 24"><path fill="#111" d="M9 0a9 9 0 0 0-9 9c0 7 9 15 9 15s9-8 9-15a9 9 0 0 0-9-9zm0 12a3 3 0 1 1 0-6 3 3 0 0 1 0 6z"/></svg></span>34, LOREM LIPSUM</li>
    <li><span class="ic"></span>903 894</li>
  </ul>

  <div class="abs bottom-bar">© 2024 BROKKHALM. ALL RIGHTS RESERVED.</div>
</footer>

</body>
</html>
```